Christmas Card for Holidays to Companies Clients

Hello designers! We are looking for the best Christmas Cards we can get to send out to our companies clients in the holidays. We don't have a lot of specifications, we just wanted to have a little detail with them for the upcoming holidays.

Our company is a technological company that offers different product, solutions and services. Most of our clients are some of the countries banks.

Colors

Designer to choose colors to be used in the design.

Requirements
Must have
• The logo and name of our company (Lumoventa) and a nice but short and precise message for the holidays.

```html
<!DOCTYPE html>
<html lang="en">
<head>
<meta charset="utf-8">
<title>Lumoventa – Holiday Card</title>
<link href="https://fonts.googleapis.com/css2?family=Cinzel:wght@500;600;700&family=Great+Vibes&display=swap" rel="stylesheet">
<style>
  :root {
    --paper: #ffffff;
    --ink: #1c1c1c;
    --festive-red: #c3262e;
    --brand-grey: #2d2d2d;
    --pine-dark: rgba(47, 96, 62, 0.85);
    --pine-mid: rgba(86, 145, 96, 0.6);
    --leaf-pale: rgba(190, 220, 195, 0.35);
    --berry: rgba(200, 54, 90, 0.55);
    --clear: rgba(255, 255, 255, 0);
    --glow: rgba(255, 240, 170, 0.75);
  }
  * { margin: 0; padding: 0; box-sizing: border-box; }
  html, body { width: 1200px; height: 857px; overflow: hidden; background: var(--paper); }
  .holiday-card {
    position: relative;
    width: 1200px;
    height: 857px;
    background: var(--paper);
    overflow: hidden;
    font-family: "Cinzel", serif;
    color: var(--ink);
  }
  .warm-glow {
    position: absolute;
    left: 380px; top: 230px;
    width: 440px; height: 380px;
    background: radial-gradient(closest-side, var(--glow) 0%, rgba(255,240,170,0.3) 45%, var(--clear) 100%);
  }
  .greenery { position: absolute; }
  .greenery--top-left {
    left: -320px; top: -320px; width: 760px; height: 840px;
    background: radial-gradient(closest-side, var(--pine-dark) 0%, var(--pine-mid) 50%, var(--leaf-pale) 78%, var(--clear) 100%);
  }
  .greenery--top-center {
    left: 330px; top: -200px; width: 540px; height: 520px;
    background: radial-gradient(closest-side, var(--berry) 0%, var(--pine-mid) 35%, var(--leaf-pale) 75%, var(--clear) 100%);
  }
  .greenery--top-right {
    left: 780px; top: -320px; width: 740px; height: 760px;
    background: radial-gradient(closest-side, var(--pine-dark) 0%, var(--pine-mid) 50%, var(--leaf-pale) 78%, var(--clear) 100%);
  }
  .greenery--bottom-left {
    left: -260px; top: 560px; width: 640px; height: 560px;
    background: radial-gradient(closest-side, var(--berry) 0%, var(--pine-mid) 40%, var(--leaf-pale) 75%, var(--clear) 100%);
  }
  .greenery--bottom-center {
    left: 300px; top: 770px; width: 600px; height: 180px;
    background: radial-gradient(closest-side, var(--leaf-pale) 0%, var(--clear) 100%);
  }
  .greenery--bottom-right {
    left: 800px; top: 560px; width: 680px; height: 560px;
    background: radial-gradient(closest-side, var(--berry) 0%, var(--pine-mid) 40%, var(--leaf-pale) 75%, var(--clear) 100%);
  }
  .greeting {
    position: absolute;
    left: 0; top: 338px;
    width: 1200px;
    text-align: center;
    font-weight: 600;
    font-size: 22.5px;
    line-height: 39px;
    letter-spacing: 0.4px;
    text-transform: lowercase;
  }
  .thank-you {
    position: absolute;
    left: 0; top: 505px;
    width: 1200px;
    text-align: center;
    font-family: "Great Vibes", cursive;
    font-size: 78px;
    line-height: 100px;
    color: var(--festive-red);
  }
  .brand {
    position: absolute;
    left: 405px; top: 674px;
    display: flex;
    align-items: center;
    gap: 16px;
  }
  .brand__dot {
    width: 84px; height: 84px;
    border-radius: 50%;
    background: var(--festive-red);
    flex: none;
  }
  .brand__text { display: flex; flex-direction: column; }
  .brand__name {
    font-family: "Cinzel", serif;
    font-weight: 700;
    font-size: 42px;
    line-height: 46px;
    color: var(--brand-grey);
    letter-spacing: 1px;
  }
  .brand__tagline {
    font-family: "Cinzel", serif;
    font-weight: 700;
    font-size: 17px;
    line-height: 24px;
    color: var(--brand-grey);
    letter-spacing: 0.5px;
  }
</style>
</head>
<body>
  <main class="holiday-card">
    <div class="greenery greenery--top-left" role="img" aria-label="Watercolour pine branches, eucalyptus leaves and red holly berries"></div>
    <div class="greenery greenery--top-right" role="img" aria-label="Watercolour pine branches, leaves and red berries"></div>
    <div class="greenery greenery--top-center" role="img" aria-label="Pine garland with red berries and a red plaid bow"></div>
    <div class="greenery greenery--bottom-left" role="img" aria-label="Pine sprigs, berries, plaid ribbon and gold snowflakes"></div>
    <div class="greenery greenery--bottom-right" role="img" aria-label="Pine sprigs, red berries, plaid bow and gold snowflakes"></div>
    <div class="greenery greenery--bottom-center" role="img" aria-label="Soft green leaves along the lower edge"></div>

    <div class="warm-glow"></div>

    <p class="greeting">
      At the holiday season, our thoughts turn<br>
      gratefully to those who have made<br>
      our progress possible<br>
      It is in this spirit we say, simply but sincerely . . .
    </p>

    <p class="thank-you">Thank you</p>

    <div class="brand">
      <span class="brand__dot"></span>
      <div class="brand__text">
        <span class="brand__name">LUMOVENTA</span>
        <span class="brand__tagline">IT CONSULTING AND SERVICES</span>
      </div>
    </div>
  </main>
</body>
</html>
```